Technology Services Fleet Wrap

We provide IT and Network Management Services to small to medium sized businesses. We would like to have our website, phone number, logo, services listed. We have a business to wrap the car but we need the design file for him to print the vinyl. Included an example picture of something we like. The blue in our logo is a color we would like to keep. The logo can be all one color it does not have to have the tech background that is currently in it

Target Market(s)

Businesses

Industry/Entity Type

Information Technology

```html
<!DOCTYPE html>
<html lang="en">
<head>
<meta charset="utf-8">
<title>Brightlane Tech – Fleet Wrap Side Panel</title>
<link rel="stylesheet" href="https://fonts.googleapis.com/css2?family=Roboto:wght@400;500;700&display=swap">
<style>
  :root {
    --brand-blue: #1a73d1;
    --brand-blue-light: #3d8fe0;
    --wrap-white: #ffffff;
    --page-bg: #ffffff;
    --panel-edge: #d9dde2;
    --outline-dark: #111111;
  }
  html, body {
    margin: 0;
    padding: 0;
    width: 1200px;
    height: 858px;
    overflow: hidden;
    background: var(--page-bg);
  }
  .wrap-canvas {
    display: block;
    width: 1200px;
    height: 858px;
    font-family: "Roboto", Arial, sans-serif;
  }
  .panel-body { fill: var(--wrap-white); stroke: var(--panel-edge); stroke-width: 1.5; }
  .blue-field { fill: var(--brand-blue); }
  .circuit-texture { fill: url(#circuitTone); }
  .swoosh-white { fill: none; stroke: var(--wrap-white); }
  .swoosh-blue { fill: none; stroke: var(--brand-blue); }
  .service-list {
    fill: var(--wrap-white);
    stroke: var(--outline-dark);
    stroke-width: 2.4;
    paint-order: stroke fill;
    font-size: 21px;
    font-weight: 500;
  }
  .brand-mark { fill: none; stroke: var(--brand-blue); stroke-width: 3; }
  .brand-name { fill: var(--brand-blue); font-size: 19px; font-weight: 500; letter-spacing: 1px; }
  .tagline { fill: var(--brand-blue); font-size: 15px; font-weight: 700; }
  .phone-pill { fill: var(--brand-blue); }
  .phone-number { fill: var(--wrap-white); font-size: 24px; font-weight: 700; letter-spacing: 0.5px; }
  .web-address { fill: var(--brand-blue); font-size: 26px; font-weight: 400; }
</style>
</head>
<body>
<svg class="wrap-canvas" viewBox="0 0 1200 858" xmlns="http://www.w3.org/2000/svg">
  <defs>
    <linearGradient id="circuitTone" x1="0" y1="0" x2="1" y2="1">
      <stop offset="0" stop-color="#3d8fe0" stop-opacity="0.55"/>
      <stop offset="1" stop-color="#1a73d1" stop-opacity="0.2"/>
    </linearGradient>
    <clipPath id="panelClip">
      <rect x="40" y="250" width="1120" height="360" rx="14"/>
    </clipPath>
  </defs>

  <rect class="panel-body" x="40" y="250" width="1120" height="360" rx="14"/>

  <g clip-path="url(#panelClip)">
    <path class="blue-field" d="M40,250 L300,250 Q390,470 600,610 L40,610 Z"/>
    <path class="circuit-texture" role="img" aria-label="Faint circuit board trace pattern across the blue field"
          d="M40,250 L250,250 Q340,460 520,610 L40,610 Z"/>
    <path class="swoosh-white" stroke-width="14" d="M256,244 Q350,470 540,616"/>
    <path class="swoosh-white" stroke-width="6" d="M292,320 Q390,500 560,616"/>
    <path class="swoosh-blue" stroke-width="4" d="M318,250 Q400,470 600,616"/>
  </g>

  <text class="service-list" x="145" y="388">YOU NEED IT</text>
  <text class="service-list" x="145" y="414">WE DESIGN IT</text>
  <text class="service-list" x="145" y="440">WE IMPLEMENT IT</text>
  <text class="service-list" x="145" y="466">WE MAINTAIN IT</text>
  <text class="service-list" x="145" y="492">WE SECURE IT</text>

  <circle class="brand-mark" cx="595" cy="365" r="64"/>
  <text class="brand-name" x="595" y="472" text-anchor="middle">BRIGHTLANE TECH</text>

  <text class="tagline" x="852" y="444" text-anchor="middle">ANY TIME!&#160; ANY WHERE!</text>
  <text class="tagline" x="852" y="463" text-anchor="middle">ANY WAY!</text>

  <rect class="phone-pill" x="740" y="475" width="222" height="31" rx="6"/>
  <text class="phone-number" x="851" y="499" text-anchor="middle">+1 555-014-2290</text>

  <text class="web-address" x="752" y="542" text-anchor="middle">WWW.BRIGHTLANETECH.COM</text>
</svg>
</body>
</html>
```